Photographic Tutorial website

We are looking for a fresh design for a photographic tutorial / workshop website. The website will have the included functions:

* Home (needs to have a login section)
* About Us
* Info about each course / workshop.
* Subscribe to courses and pay online.
* Members Area
* Photo gallery
* Contact us

The website will be implemented with our own made cms. We do not need it to be coded. We have a team ready to do this for us. We only need the PSD layout.

We have attached a mockup design that the client and I have come up with and we need the design to be taken to the next level.

Client also likes:
http://www.lumavistacamera.example/

Requirements
Must have
• Must Stand out i.e black backgrounds
Should not have
• Alter the logo in anyway.

```html
<!DOCTYPE html>
<html lang="en">
<head>
<meta charset="utf-8">
<title>Frame Mentor – Photographic Tuition</title>
<link rel="stylesheet" href="https://fonts.googleapis.com/css2?family=Noto+Serif:wght@400;700&family=Kaushan+Script&family=Arimo:wght@400;700&display=swap">
<style>
:root{
  --bg:#000;
  --panel:#2e2e2e;
  --panel-line:#555;
  --green:#3fa33a;
  --green-text:#4cbb3f;
  --orange:#f07a10;
  --orange-btn:#e98410;
  --red:#e0201a;
  --text:#ddd;
  --footer-band:#3b3b3b;
  --serif:'Noto Serif', Georgia, serif;
}
*{box-sizing:border-box;margin:0;padding:0}
html,body{width:924px;height:1200px;overflow:hidden;background:var(--bg);font-family:var(--serif);color:var(--text)}
.page{position:relative;width:924px;height:1200px;overflow:hidden}
.abs{position:absolute}

.site-header{left:0;top:0;width:924px;height:86px;background:repeating-linear-gradient(45deg,#1e1e1e 0 2px,#191919 2px 4px)}
.brand{left:50px;top:18px;display:flex;align-items:center;gap:8px}
.brand-mark{width:30px;height:30px;border-radius:50%;background:var(--red)}
.brand-name{font-size:28px;font-weight:700;color:#fff;line-height:1}
.brand-tag{left:90px;top:54px;font-size:10px;letter-spacing:4px;color:#fff}
.member-login{right:54px;top:44px;font-size:12.5px;color:var(--green-text);display:flex;align-items:center;gap:8px}

.hero{left:46px;top:86px;width:828px;height:408px;background:radial-gradient(ellipse at 70% 40%,#2e6b3c 0%,#1d4a2a 50%,#0d2414 100%)}
.hero-title{left:290px;top:100px;font-family:'Kaushan Script',cursive;font-size:52px;color:#fff}
.hero-dots{left:66px;top:478px;display:flex;gap:4px}
.hero-dots span{width:9px;height:9px;border-radius:50%;background:var(--green)}
.hero-dots span:first-child{background:var(--red)}

.hero-fade{left:46px;top:494px;width:828px;height:100px;background:linear-gradient(#151515,#000)}
.main-nav{left:46px;top:517px;width:828px;height:33px;background:linear-gradient(#4a4a4a,#2a2a2a)}
.main-nav a{position:absolute;top:0;font-size:13px;color:#fff;text-decoration:none;line-height:33px;white-space:nowrap}
.main-nav a.active{color:var(--green-text)}
.main-nav i{position:absolute;top:0;width:2px;height:33px;background:#777}
.search{left:672px;top:522px;width:178px;height:24px;display:flex}
.search span{flex:1;background:#111;font-size:12px;color:#fff;padding:4px 8px}
.search b{width:30px;background:#222;border-left:2px solid #555}

.widget{background:var(--panel);border-radius:8px}
.widget h3{font-weight:400;font-size:12px;color:var(--green-text);line-height:18px;white-space:nowrap}
.widget hr{border:0;border-top:2px solid var(--panel-line);position:absolute;left:0;right:0}
.w-times{left:50px;top:592px;width:182px;height:186px}
.w-moon{left:275px;top:592px;width:376px;height:186px}
.w-check{left:694px;top:592px;width:181px;height:186px}
.label{position:absolute;font-size:11.5px;color:#bbb;white-space:nowrap}
.box{position:absolute;background:#888;color:#fff;font-size:9.5px;height:16px;line-height:16px;padding:0 3px;white-space:nowrap}
.sel{position:absolute;background:#111;width:20px;height:16px}
.sel::after{content:"";position:absolute;left:5px;top:5px;border:5px solid transparent;border-top:6px solid var(--green-text)}
.btn{position:absolute;background:var(--orange-btn);color:#000;font-size:10.5px;line-height:16px;height:16px;text-align:center;white-space:nowrap}
.check li{list-style:none;font-size:11px;color:#aaa;line-height:27px}

.gallery{left:41px;top:802px;width:843px;height:163px;background:#171717}
.gallery h3{left:42px;top:8px;font-weight:400;font-size:13px;color:var(--green-text)}
.arrow{top:32px;width:34px;height:96px;background:#2e2e2e}
.thumb{top:32px;height:96px}
.caption{top:137px;font-size:10.5px;color:#fff;text-align:center}

.footer-band{left:0;top:993px;width:924px;height:153px;background:var(--footer-band)}
.fbox{top:1011px;height:117px;background:linear-gradient(#555,#3b3b3b 40%)}
.fbox h4{font-weight:400;font-size:13px;color:#bbb;white-space:nowrap}
.mgrid{left:55px;top:1050px;display:grid;grid-template-columns:repeat(4,56px);gap:3px 2px}
.mgrid div{height:36px}
.testi{font-size:10.3px;line-height:18px;color:#fff}
.testi a{color:var(--orange);text-decoration:none}
.links li{list-style:none;font-size:12px;color:#fff;line-height:21.5px;white-space:nowrap}

.copyright{left:49px;top:1171px;font-family:'Arimo',sans-serif;font-size:10px;color:#fff}
.copyright b{color:var(--orange);font-weight:400}
.social{left:788px;top:1158px;width:98px;height:32px;background:#1c1c1c;font-size:11px;color:#4a7fd0;display:flex;align-items:center;gap:5px;padding-left:6px}
.social i{width:20px;height:20px;background:#3b5a9a;display:block}
</style>
</head>
<body>
<div class="page">
  <header class="site-header abs">
    <div class="brand abs"><span class="brand-mark"></span><span class="brand-name">Frame Mentor</span></div>
    <div class="brand-tag abs">PHOTOGRAPHIC TUITION</div>
    <div class="member-login abs">
      <svg width="28" height="18" viewBox="0 0 28 18" fill="#fff"><circle cx="8" cy="5" r="3.5"/><circle cx="20" cy="5" r="3.5"/><circle cx="14" cy="6" r="4"/><path d="M2 17c0-5 3-7 6-7s6 2 6 7zM14 17c0-5 3-7 6-7s6 2 6 7zM7 18c0-6 3-8 7-8s7 2 7 8z"/></svg>
      Member Login
    </div>
  </header>

  <div class="hero abs" role="img" aria-label="Photographer holding a camera beside a large butterfly on a leaf, dark green backdrop"></div>
  <div class="hero-title abs">Daniel Ashby 2012</div>
  <div class="hero-dots abs"><span></span><span></span><span></span><span></span></div>

  <div class="hero-fade abs"></div>
  <nav class="main-nav abs">
    <a class="active" style="left:21px">Home</a><i style="left:78px"></i>
    <a style="left:96px">About Us</a><i style="left:167px"></i>
    <a style="left:180px">Our courses <span style="color:var(--green-text)">&#11015;</span></a><i style="left:282px"></i>
    <a style="left:295px">Members Area</a><i style="left:402px"></i>
    <a style="left:418px">Contact us</a>
  </nav>
  <div class="search abs"><span>Search...</span><b><svg width="28" height="24" viewBox="0 0 28 24"><circle cx="12" cy="10" r="5" fill="none" stroke="#4cbb3f" stroke-width="2.5"/><path d="M16 14l6 5" stroke="#4cbb3f" stroke-width="3"/></svg></b></div>

  <section class="widget w-times abs">
    <h3 class="abs" style="left:9px;top:5px">Daily shooting times<br>Nautical twilight start to End</h3>
    <hr style="top:44px">
    <svg class="abs" style="left:12px;top:50px" width="44" height="42" viewBox="0 0 44 42"><circle cx="20" cy="22" r="17" fill="#eee" stroke="#999" stroke-width="2"/><path d="M20 22V11M20 22h8" stroke="#333" stroke-width="2"/><circle cx="30" cy="31" r="8" fill="#222"/><path d="M28 27l6 4-6 4z" fill="#fff"/></svg>
    <div class="abs" style="left:74px;top:74px;font-size:11px;color:var(--red);white-space:nowrap">Morning 5:00 AM</div>
    <p class="abs" style="left:7px;top:92px;width:168px;font-size:10.5px;line-height:18px;color:#fff">Lorem ipsum dolor sit amet, consectetur adipiscing elit. Mauris tincidunt feugiat felis ut fermentum. Etiam nec ipsum eu tortor interdum dictum.</p>
  </section>

  <section class="widget w-moon abs">
    <h3 class="abs" style="left:10px;top:24px">Moon Phase chart</h3>
    <hr style="top:47px;right:170px">
    <div class="label" style="left:6px;top:54px">Date</div>
    <div class="box" style="left:34px;top:54px;width:52px">03/04/2005</div>
    <div class="label" style="left:89px;top:54px">Time</div>
    <div class="box" style="left:120px;top:54px;width:50px;text-align:center">4:32 AM</div>
    <div class="btn" style="left:173px;top:54px;width:28px">New</div>

    <div class="label" style="left:6px;top:79px">Time Zone :</div>
    <div class="box" style="left:99px;top:79px;width:79px">-7:00 (MST)</div>
    <div class="sel" style="left:178px;top:79px"></div>

    <div class="label" style="left:6px;top:106px">Latitude :</div>
    <div class="box" style="left:90px;top:106px;width:22px">40</div>
    <div class="box" style="left:115px;top:106px;width:22px">32</div>
    <div class="box" style="left:139px;top:106px;width:21px">0</div>
    <div class="box" style="left:162px;top:106px;width:16px">N</div>
    <div class="sel" style="left:178px;top:106px"></div>

    <div class="label" style="left:6px;top:133px">Longitude :</div>
    <div class="box" style="left:90px;top:133px;width:22px">112</div>
    <div class="box" style="left:115px;top:133px;width:22px">18</div>
    <div class="box" style="left:139px;top:133px;width:21px">0</div>
    <div class="box" style="left:162px;top:133px;width:16px">W</div>
    <div class="sel" style="left:178px;top:133px"></div>

    <div class="btn" style="left:155px;top:160px;width:45px">Apply</div>
    <div class="abs" style="left:206px;top:10px;width:163px;height:167px;background:radial-gradient(circle,#ccc 0 28%,#777 42%,#000 44%)" role="img" aria-label="Labelled moon phase chart showing lunar seas"></div>
  </section>

  <section class="widget w-check abs">
    <h3 class="abs" style="left:12px;top:24px">Photograpers check lists</h3>
    <hr style="top:47px">
    <ul class="check abs" style="left:14px;top:84px"><li>1 . Wedding shoot checklist</li><li>2 . Pre shoot checklist</li><li>3 . Standard checklist</li></ul>
  </section>

  <section class="gallery abs">
    <h3 class="abs">Photo Gallery</h3>
    <div class="arrow abs" style="left:6px"><svg width="34" height="96"><path d="M22 38l-8 10 8 10" stroke="#666" stroke-width="3" fill="none"/></svg></div>
    <div class="thumb abs" style="left:41px;width:119px;background:linear-gradient(#e9b8a0,#6f7fa0 60%,#3a2f2c)" role="img" aria-label="Jetty stretching into the sea at dusk"></div>
    <div class="thumb abs" style="left:168px;width:119px;background:linear-gradient(#3c6da8,#8ab0d4 40%,#1d4f84)" role="img" aria-label="Panorama of a calm bay under blue sky"></div>
    <div class="thumb abs" style="left:296px;width:248px;background:linear-gradient(#1a2a4c,#3a4a6c 50%,#c97a3a 70%,#111)" role="img" aria-label="City skyline lights at night across water"></div>
    <div class="thumb abs" style="left:553px;width:119px;background:linear-gradient(#6f8fb4,#3d5068 60%,#2f4a2a)" role="img" aria-label="Tall office tower seen from street level"></div>
    <div class="thumb abs" style="left:682px;width:119px;background:linear-gradient(#d8d8d0,#a88a5a 50%,#3a6a2a)" role="img" aria-label="Heritage building with red flower in HDR"></div>
    <div class="arrow abs" style="left:803px"><svg width="34" height="96"><path d="M12 38l8 10-8 10" stroke="#666" stroke-width="3" fill="none"/></svg></div>
    <div class="caption abs" style="left:41px;width:119px">Urdan Excursion</div>
    <div class="caption abs" style="left:168px;width:119px">Panorama</div>
    <div class="caption abs" style="left:296px;width:248px">Night Photography &amp; City Lights</div>
    <div class="caption abs" style="left:553px;width:119px">City Walks</div>
    <div class="caption abs" style="left:682px;width:119px">HDR</div>
  </section>

  <div class="footer-band abs"></div>
  <section class="fbox abs" style="left:49px;width:243px">
    <h4 class="abs" style="left:7px;top:16px">Member Gallery</h4>
    <div class="btn" style="left:176px;top:11px;width:66px;height:19px;line-height:19px">View More</div>
  </section>
  <div class="mgrid abs" role="img" aria-label="Grid of eight member photographs">
    <div style="background:#a04a1a"></div><div style="background:#c9a88a"></div><div style="background:#c85a1a"></div><div style="background:#4a3a2a"></div>
    <div style="background:#2a3a5a"></div><div style="background:#1a3a7a"></div><div style="background:#a08a4a"></div><div style="background:#7a6aa0"></div>
  </div>
  <section class="fbox abs" style="left:346px;width:244px">
    <h4 class="abs" style="left:10px;top:17px">Testimonials</h4>
    <p class="testi abs" style="left:11px;top:50px;width:226px">Frame Mentor photographic workshop have provided excellent training and I can show off my pictures to my friends and family members. <a>Read More...</a></p>
  </section>
  <section class="fbox abs" style="left:631px;width:244px">
    <div class="abs" style="left:13px;top:10px;width:105px;height:111px;background:linear-gradient(135deg,#e8ecee,#c8d4dc)" role="img" aria-label="Road map of a touring route"></div>
    <ul class="links abs" style="left:126px;top:14px"><li>Photography Blog</li><li>General Information</li><li>&amp; FM's 2012</li><li>USA Fall Tour</li><li>Travel Blog</li></ul>
  </section>

  <footer>
    <div class="copyright abs">Copyright © 2012 &nbsp;<b>Frame Mentor</b> . Privacy Policy | Terms &amp; Conditions</div>
    <div class="social abs"><i></i>Friendwall</div>
  </footer>
</div>
</body>
</html>
```